CSS Template Layout

We are looking for a page design template that we can update our site. Here are the requirements.

We need a header image across the top and three columns below. Layout should be controlled by css, not tables.

This is for a landscape/snow removal directory. A generic layout for overall size can be found at www.brindlemeadowyards.example Images should relate to lawns/landscaping/snow removal.

We do not have a logo at this time, so we will simply be using a font with the site name. The site should be colorful and inviting, it should feel fresh and clean. These are landscapers and they groom the beauty found in nature.

Do not hesitate to ask questions or bounce ideas off of us.
Updates

Project Deadline Extended
Reason: We are sorry but we need to extend the deadline, we inadvertently deadlined on a Saturday and will not be in the office. We have internally worked out our schedules to meet next thursday. On the plus side, we are guaranteeing payment based on the two designs submitted already.

```html
<!DOCTYPE html>
<html lang="en">
<head>
<meta charset="utf-8">
<title>Local Landscape Service</title>
<link href="https://fonts.googleapis.com/css2?family=Open+Sans:wght@400;700&display=swap" rel="stylesheet">
<style>
  :root {
    --brand-green: #80c91a;
    --title-green: #7cc520;
    --nav-blue: #0a5bbf;
    --heading-blue: #1668c2;
    --drop-cyan: #00b3e8;
    --text-dark: #1f1f1f;
    --social-one: #0b61a8;
    --social-two: #1c3f94;
    --social-three: #1da1e8;
    --white: #ffffff;
    --grass-light: #8fd12a;
    --grass-dark: #3f8a12;
  }
  * { margin: 0; padding: 0; box-sizing: border-box; }
  html, body {
    width: 1200px; height: 750px; overflow: hidden;
    background: var(--white);
    font-family: "Open Sans", Arial, sans-serif;
    color: var(--text-dark);
  }
  .page { position: relative; width: 1200px; height: 750px; }
  .hero {
    position: absolute; left: 0; top: 0; width: 1200px; height: 215px;
    background: linear-gradient(180deg, var(--grass-dark) 0%, var(--grass-light) 55%, var(--grass-dark) 100%);
  }
  .site-title {
    position: absolute; left: 304px; top: 230px;
    font-size: 23px; font-weight: 700; letter-spacing: 0.3px;
    color: var(--title-green); text-transform: uppercase;
  }
  .main-nav { position: absolute; left: 304px; top: 280px; display: flex; gap: 8px; }
  .nav-item {
    width: 92px; height: 43px; background: var(--nav-blue);
    color: var(--white); font-size: 11px;
    display: flex; align-items: center; justify-content: center;
  }
  .nav-item.is-active { background: var(--brand-green); color: var(--text-dark); }
  .columns { position: absolute; left: 304px; top: 344px; display: flex; gap: 8px; }
  .service { width: 192px; }
  .service h2 {
    font-size: 13.5px; font-weight: 700; color: var(--heading-blue);
    text-transform: uppercase; line-height: 18px; margin-bottom: 14px;
  }
  .service p { font-size: 9.6px; line-height: 12.9px; }
  .dropdown { position: absolute; left: 404px; top: 331px; z-index: 2; }
  .dropdown-item {
    width: 92px; height: 22px; margin-bottom: 8px;
    background: var(--drop-cyan); color: var(--white);
    font-size: 8px; padding-left: 10px; display: flex; align-items: center;
  }
  .social { position: absolute; left: 754px; top: 537px; display: flex; gap: 7px; }
  .social-tile {
    width: 43px; height: 43px; color: var(--white);
    font-size: 8px; font-weight: 700;
    display: flex; align-items: center; justify-content: center;
  }
  .social-netlink { background: var(--social-one); }
  .social-friendo { background: var(--social-two); }
  .social-chirpy { background: var(--social-three); }
  .footer-bar {
    position: absolute; left: 304px; top: 601px; width: 592px; height: 43px;
    background: var(--brand-green);
  }
</style>
</head>
<body>
<div class="page">
  <div class="hero" role="img" aria-label="Photograph of a freshly mowed lawn with alternating light and dark green stripes"></div>

  <h1 class="site-title">Local Landscape Service</h1>

  <nav class="main-nav">
    <div class="nav-item">Home</div>
    <div class="nav-item is-active">About Us</div>
    <div class="nav-item">Search</div>
    <div class="nav-item">Register</div>
    <div class="nav-item">Login</div>
    <div class="nav-item">Contact</div>
  </nav>

  <div class="dropdown">
    <div class="dropdown-item">Company</div>
    <div class="dropdown-item">Clients</div>
    <div class="dropdown-item">Portfolio</div>
  </div>

  <section class="columns">
    <article class="service">
      <h2>Lawn Service</h2>
      <p>Lorem ipsum dolor sit amet, consectetur adipisicing elit, sed do eiusmod tempor incididunt ut labore et dolore magna aliqua. Ut enim ad minim veniam, quis nostrud exercitation ullamco laboris nisi ut aliquip ex ea commodo consequat. Duis aute irure dolor in reprehenderit in voluptate velit esse cillum dolore eu fugiat nulla pariatur. Excepteur sint occaecat cupidatat non proident, sunt in culpa qui officia deserunt mollit anim id est laborum.</p>
    </article>
    <article class="service">
      <h2>Landscaping Service</h2>
      <p>Lorem ipsum dolor sit amet, consectetur adipisicing elit, sed do eiusmod tempor incididunt ut labore et dolore magna aliqua. Ut enim ad minim veniam, quis nostrud exercitation ullamco laboris nisi ut aliquip ex ea commodo consequat. Duis aute irure dolor in reprehenderit in voluptate velit esse cillum dolore eu fugiat nulla pariatur. Excepteur sint occaecat cupidatat non proident, sunt in culpa qui officia deserunt mollit anim id est laborum.</p>
    </article>
    <article class="service">
      <h2>Snow Removal Service</h2>
      <p>Lorem ipsum dolor sit amet, consectetur adipisicing elit, sed do eiusmod tempor incididunt ut labore et dolore magna aliqua. Ut enim ad minim veniam, quis nostrud exercitation ullamco laboris nisi ut aliquip ex ea commodo consequat. Duis aute irure dolor in reprehenderit in voluptate velit esse cillum dolore eu fugiat nulla pariatur. Excepteur sint occaecat cupidatat non proident, sunt in culpa qui officia deserunt mollit anim id est laborum.</p>
    </article>
  </section>

  <div class="social">
    <div class="social-tile social-netlink">Netlink</div>
    <div class="social-tile social-friendo">Friendo</div>
    <div class="social-tile social-chirpy">Chirpy</div>
  </div>

  <footer class="footer-bar"></footer>
</div>
</body>
</html>
```